Whitmore Business Card Design

The name of the business is Dara Whitmore, CPA LLC
The service that we offer is Accounting, Tax & Consulting Services. I need it to have the following items:
Dara Whitmore, Principal
Phone Number
Email Address
Physical Address

I have attached the company logo, one in black and one in white. Please provide a design in black background and the other in white background. Please include "Accounting, Tax & Consulting Services". I want the business card to be clean and very professional.

```html
<!DOCTYPE html>
<html lang="en">
<head>
<meta charset="utf-8">
<title>Dara Whitmore, CPA LLC — Business Cards</title>
<link rel="stylesheet" href="https://fonts.googleapis.com/css2?family=Montserrat:wght@500;600;700&display=swap">
<style>
  :root {
    --page-bg: #e8e8e9;
    --card-black: #000000;
    --card-white: #ffffff;
    --brand-red: #9b1c20;
    --ink-dark: #3a3a3a;
    --ink-grey: #808080;
    --divider: #d4d4d4;
    --white: #ffffff;
  }
  * { margin: 0; padding: 0; box-sizing: border-box; }
  html, body {
    width: 1200px;
    height: 1200px;
    overflow: hidden;
    background: var(--page-bg);
    font-family: "Montserrat", Arial, sans-serif;
  }
  .card {
    position: absolute;
    left: 188px;
    width: 832px;
    height: 486px;
  }
  .card--front { top: 82px; background: var(--card-black); color: var(--white); }
  .card--back { top: 620px; background: var(--card-white); }

  /* Shared brand lockup */
  .brand-name {
    display: inline-flex;
    align-items: center;
    gap: 14px;
    font-weight: 600;
    text-transform: uppercase;
    white-space: nowrap;
    line-height: 1.2;
  }
  .brand-mark {
    width: 0.62em;
    height: 0.62em;
    background: var(--brand-red);
  }
  .brand-descriptor {
    text-transform: uppercase;
    font-weight: 600;
    white-space: nowrap;
    line-height: 1.2;
  }

  /* Front */
  .front-identity {
    position: absolute;
    left: 0; right: 0;
    top: 168px;
    text-align: center;
  }
  .card--front .brand-name { font-size: 35px; letter-spacing: 0.01em; color: var(--white); }
  .card--front .brand-descriptor {
    margin-top: 10px;
    font-size: 25px;
    letter-spacing: 0.075em;
    color: var(--white);
  }
  .services {
    position: absolute;
    left: 0; right: 0;
    top: 384px;
    text-align: center;
    font-size: 20px;
    font-weight: 500;
    letter-spacing: 0.28em;
    text-transform: uppercase;
    white-space: nowrap;
  }

  /* Back */
  .back-identity {
    position: absolute;
    left: 0;
    width: 412px;
    top: 212px;
    text-align: center;
  }
  .card--back .brand-name { font-size: 23px; gap: 9px; color: var(--ink-dark); }
  .card--back .brand-descriptor {
    margin-top: 4px;
    font-size: 16px;
    letter-spacing: 0.11em;
    color: var(--ink-grey);
  }
  .divider {
    position: absolute;
    left: 412px;
    top: 72px;
    width: 1px;
    height: 346px;
    background: linear-gradient(to bottom, transparent, var(--divider) 20%, var(--divider) 80%, transparent);
  }
  .contact {
    position: absolute;
    left: 451px;
    top: 114px;
    color: var(--ink-dark);
  }
  .contact-name {
    font-size: 31px;
    font-weight: 600;
    text-transform: uppercase;
    line-height: 1.2;
  }
  .contact-role {
    margin-top: 8px;
    font-size: 18px;
    font-weight: 600;
    letter-spacing: 0.12em;
    text-transform: uppercase;
  }
  .contact-address {
    margin-top: 46px;
    font-style: normal;
    font-size: 17px;
    font-weight: 500;
    line-height: 30px;
  }
  .contact-list { list-style: none; margin-top: 12px; }
  .contact-item {
    display: flex;
    align-items: center;
    gap: 16px;
    height: 36px;
    font-size: 17px;
    font-weight: 500;
    padding-left: 16px;
  }
  .contact-icon { width: 20px; height: 16px; fill: var(--brand-red); flex: none; }
</style>
</head>
<body>

<section class="card card--front" aria-label="Business card front">
  <div class="front-identity">
    <div class="brand-name"><span class="brand-mark"></span>Dara Whitmore, CPA LLC</div>
    <div class="brand-descriptor">Certified Public Accountant</div>
  </div>
  <p class="services">Accounting, Tax &amp; Consulting Services</p>
</section>

<section class="card card--back" aria-label="Business card back">
  <div class="back-identity">
    <div class="brand-name"><span class="brand-mark"></span>Dara Whitmore, CPA LLC</div>
    <div class="brand-descriptor">Certified Public Accountant</div>
  </div>

  <div class="divider"></div>

  <div class="contact">
    <h1 class="contact-name">Dara Whitmore</h1>
    <p class="contact-role">Principal</p>
    <address class="contact-address">
      14 North Tower, Harbour Trade Centre,<br>
      Meridian Square, Colombo 03, Sri Lanka
    </address>
    <ul class="contact-list">
      <li class="contact-item">
        <svg class="contact-icon" viewBox="0 0 20 16" aria-hidden="true">
          <path d="M1 5 C4 1 16 1 19 5 L16 7 L14 4 C11 3 9 3 6 4 L4 7 Z"/>
          <path d="M5 8 L7 5 H13 L15 8 V15 H5 Z"/>
        </svg>
        <span>+94 11 2836014</span>
      </li>
      <li class="contact-item">
        <svg class="contact-icon" viewBox="0 0 20 16" aria-hidden="true">
          <path d="M1 2 H19 V14 H1 Z M2.5 3.5 L10 9.5 L17.5 3.5 Z M2.5 12.5 H17.5 L12 7.8 L10 9.5 L8 7.8 Z" fill-rule="evenodd"/>
        </svg>
        <span>dwcpa@dwcpa.com</span>
      </li>
    </ul>
  </div>
</section>

</body>
</html>
```